HOME IMPROVEMENT Business Card

I want a very unique business card. nothing typical and boring. Im open to you ideas. Ive seen cards with gold and silver or color foil and spot UV coatings. Im looking for something that looks cool and grabs attention. I like rounded corners but am open to all suggestions. We are a home improvement company and I will have a presentation folder printed and a catalog printed also and want to keep that same theme. I love the colors in our logo but I am open at looking at a 3rd color that would work with my logo. I hope that helps.
Card should include
Address
Phone
Fax
Email
Website
Target Market(s)
Home owners, people looking to remodel their home
Industry/Entity Type
Home Improvement
Contact Information for Business Card
2873 Maple Crest Avenue Unit 410
Des Plaines, Il 60284
Phone
Direct Line
Email
Website
Font styles to use
Other font styles liked:
- IM OPEN MINDED
Requirements
Must have
- High end quality look nothing boring I like rounded corners but am open minded
Nice to have
- WOW. I want something nice and impressive.
Should not have
- ??? Not sure

```html
<!DOCTYPE html>
<html lang="en">
<head>
<meta charset="utf-8">
<title>Brightwall Renovation Co – Business Card</title>
<link rel="stylesheet" href="https://fonts.googleapis.com/css2?family=Jost:wght@400;500;800&display=swap">
<style>
  :root {
    --bg: #3a2a3a;
    --card: #ffffff;
    --navy: #14152e;
    --green: #17992f;
    --ink: #2a2a2a;
    --rule: #1d1d1d;
  }
  * { margin: 0; padding: 0; box-sizing: border-box; }
  html, body {
    width: 1200px;
    height: 800px;
    overflow: hidden;
  }
  body {
    background: var(--bg);
    font-family: "Jost", sans-serif;
    position: relative;
  }
  .card {
    position: absolute;
    top: 252px;
    width: 520px;
    height: 297px;
    background: var(--card);
    border-radius: 14px;
    box-shadow: 0 10px 30px rgba(0,0,0,0.35);
    overflow: hidden;
  }
  .card--back { left: 50px; }
  .card--front { left: 630px; }

  .brand {
    display: flex;
    align-items: center;
    gap: 10px;
    color: var(--navy);
    font-weight: 800;
    letter-spacing: -0.3px;
    line-height: 1.1;
  }
  .brand__mark {
    background: var(--green);
    flex: none;
  }

  .card--front .brand {
    position: absolute;
    left: 0; right: 0; top: 0; bottom: 0;
    justify-content: center;
    font-size: 44px;
  }
  .card--front .brand__name { max-width: 300px; }
  .card--front .brand__mark { width: 22px; height: 22px; }

  .card--back .brand {
    position: absolute;
    left: 30px;
    top: 50%;
    transform: translateY(-50%);
    width: 205px;
    font-size: 25px;
  }
  .card--back .brand__mark { width: 14px; height: 14px; }

  .divider {
    position: absolute;
    left: 262px;
    top: 62px;
    width: 1.5px;
    height: 172px;
    background: var(--rule);
  }

  .contact {
    position: absolute;
    left: 292px;
    top: 56px;
  }
  .contact__name {
    color: var(--green);
    font-size: 30px;
    font-weight: 400;
    letter-spacing: 3px;
    line-height: 1;
  }
  .contact__role {
    color: var(--ink);
    font-size: 19px;
    font-weight: 400;
    margin-top: 4px;
    margin-bottom: 12px;
  }
  .contact__list { list-style: none; }
  .contact__item {
    display: flex;
    align-items: center;
    gap: 16px;
    color: var(--ink);
    font-size: 18px;
    margin-bottom: 10px;
  }
  .contact__icon {
    width: 30px;
    height: 30px;
    flex: none;
  }
</style>
</head>
<body>

  <section class="card card--back" aria-label="Business card back">
    <div class="brand">
      <span class="brand__mark"></span>
      <span class="brand__name">Brightwall Renovation Co</span>
    </div>

    <div class="divider"></div>

    <div class="contact">
      <p class="contact__name">NAME</p>
      <p class="contact__role">Position</p>
      <ul class="contact__list">
        <li class="contact__item">
          <svg class="contact__icon" viewBox="0 0 30 30" aria-hidden="true">
            <circle cx="15" cy="15" r="15" fill="#17992f"/>
            <path d="M11 8 q-3 1 -2 5 q2 6 8 9 q3 1 4 -1 l-2.5 -2.5 l-2 1 q-3 -2 -4.5 -5 l1.5 -1.5 z" fill="#fff"/>
          </svg>
          <span>Phone</span>
        </li>
        <li class="contact__item">
          <svg class="contact__icon" viewBox="0 0 30 30" aria-hidden="true">
            <circle cx="15" cy="15" r="15" fill="#17992f"/>
            <rect x="8" y="10" width="14" height="10" fill="none" stroke="#fff" stroke-width="1.6"/>
            <path d="M8 10 l7 6 l7 -6" fill="none" stroke="#fff" stroke-width="1.6"/>
          </svg>
          <span>Mail</span>
        </li>
        <li class="contact__item">
          <svg class="contact__icon" viewBox="0 0 30 30" aria-hidden="true">
            <circle cx="15" cy="15" r="15" fill="#17992f"/>
            <path d="M7 15 l8 -7 l8 7" fill="none" stroke="#fff" stroke-width="2"/>
            <path d="M10 14 v8 h10 v-8" fill="none" stroke="#fff" stroke-width="2"/>
            <rect x="13.5" y="17" width="3" height="5" fill="#fff"/>
          </svg>
          <span>Address</span>
        </li>
      </ul>
    </div>
  </section>

  <section class="card card--front" aria-label="Business card front">
    <div class="brand">
      <span class="brand__mark"></span>
      <span class="brand__name">Brightwall Renovation Co</span>
    </div>
  </section>

</body>
</html>
```